Quarterly Growth Letter needs a Letterhead

Our firm, BRV Solutions produces "Tobias's Quarterly Growth Letter", a monthly digest of marketing tips and tips for business owners in the MENA region. We use Postlyne to distribute this memo to our database each month. We are looking for a designer to put together a letterhead for this memo.

The goal of the memo is to produce original, relevant, and new content to readers. We are a quickly adapting company. We provide fresh material, and the branding and logo of the newsletter heading should reflect this.

What the letterhead should include:
- Our BRV Solutions logo (provided by me)
- The words "Tobias's Quarterly Growth Letter"
- Tobias's picture (provided by me)

It should be in a jpg or png format so that I can load it into the Postlyne template. The template is designed to be a traditional A4 in width.

To receive our logo and Tobias's picture for your design, please email me at jordan@brvsolutions.example.

Target Market(s)

Companies in the MENA region that are looking to dramatically improve their sales and marketing.

Industry/Entity Type

Marketing

Requirements
Must have
• The letterhead must be neat and have a clean design.
Should not have
• Too many colors, swirls or soft fonts.

```html
<!DOCTYPE html>
<html lang="en">
<head>
<meta charset="utf-8">
<title>BRV Solutions – Stationery</title>
<link rel="stylesheet" href="https://fonts.googleapis.com/css2?family=Open+Sans:wght@300;400;600;700&display=swap">
<style>
  :root {
    --bg: #ececec;
    --paper: #ffffff;
    --brand-blue: #4f9bd9;
    --brand-gray: #8c8d8f;
    --ink: #6f7072;
    --ink-soft: #9a9b9d;
    --photo-a: #c9b7a6;
    --photo-b: #3d3f46;
  }
  * { box-sizing: border-box; margin: 0; padding: 0; }
  html, body { width: 1200px; height: 798px; overflow: hidden; }
  body {
    background: var(--bg);
    font-family: "Open Sans", Arial, sans-serif;
    color: var(--ink);
    position: relative;
  }
  .sheet {
    position: absolute;
    background: var(--paper);
    box-shadow: 0 4px 14px rgba(0,0,0,.12);
    overflow: hidden;
  }
  .letterhead { left: 60px; top: 29px; width: 523px; height: 740px; }
  .envelope { width: 540px; height: 250px; }
  .envelope--window { left: 620px; top: 100px; }
  .envelope--plain { left: 620px; top: 430px; }

  .company-name {
    position: absolute;
    font-size: 22px;
    font-weight: 600;
    color: var(--ink);
    line-height: 1;
    white-space: nowrap;
  }
  .letterhead .company-name { left: 34px; top: 38px; }
  .envelope .company-name { left: 30px; top: 30px; }

  .memo-title {
    position: absolute; right: 34px; top: 96px;
    font-size: 13px; font-weight: 600; color: var(--brand-blue);
  }
  .letter-body { position: absolute; left: 60px; right: 60px; top: 130px; }
  .letter-body h1 {
    font-size: 20px; font-weight: 300; color: var(--ink-soft); margin-bottom: 14px;
  }
  .letter-body p {
    font-size: 9px; line-height: 1.55; color: var(--ink-soft); margin-bottom: 10px;
  }

  .footer-band { position: absolute; left: 0; bottom: 0; width: 100%; }
  .letterhead .footer-band { height: 200px; }
  .envelope .footer-band { height: 130px; }

  .portrait {
    position: absolute;
    border: 3px solid var(--brand-blue);
    background: linear-gradient(180deg, var(--photo-a) 0%, var(--photo-a) 45%, var(--photo-b) 100%);
  }
  .letterhead .portrait { left: 46px; top: 520px; width: 62px; height: 70px; }
  .envelope .portrait { left: 26px; top: 88px; width: 58px; height: 64px; }

  .contact {
    position: absolute; right: 26px; text-align: right;
    color: #fff; font-size: 10px; line-height: 1.45;
  }
  .letterhead .contact { bottom: 14px; }
  .envelope .contact { bottom: 12px; font-size: 9.5px; }

  .address-window {
    position: absolute; right: 40px; top: 128px; width: 180px; height: 74px;
    background: #f1f1f1; border: 1px solid #dcdcdc; border-radius: 6px;
  }
</style>
</head>
<body>

  <section class="sheet letterhead">
    <div class="company-name">BRV Solutions</div>
    <div class="memo-title">Tobias's Quarterly Growth Letter</div>

    <article class="letter-body">
      <h1>Lorem ipsum dolor sit amet</h1>
      <p>Each quarter we share practical ideas that help growing companies sharpen their message, reach the right buyers and turn steady attention into lasting sales across the region.</p>
      <p>This issue looks at simple campaign planning, clear offers and the small weekly habits that keep a sales pipeline healthy when markets shift quickly and budgets tighten.</p>
      <p>We also review three client stories, share a short checklist for landing pages and explain how to measure what matters before spending more on advertising.</p>
      <p>Reply to this letter with your questions and we will answer the most useful ones in the next edition.</p>
    </article>

    <svg class="footer-band" viewBox="0 0 523 200" preserveAspectRatio="none" aria-hidden="true">
      <path d="M0,40 Q260,92 523,118 V200 H0 Z" fill="var(--brand-blue)"/>
      <path d="M0,60 Q260,114 523,136 V200 H0 Z" fill="var(--brand-gray)"/>
    </svg>
    <div class="portrait" role="img" aria-label="Portrait photo of Tobias"></div>
    <div class="contact">
      Call: xxxxxxxxx | Fax: xxxxxxx<br>
      Mail: hello@brvsolutions.example | www.brvsolutions.example<br>
      24 Harbor Lane, Eastfield, 40210
    </div>
  </section>

  <section class="sheet envelope envelope--window">
    <div class="company-name">BRV Solutions</div>
    <svg class="footer-band" viewBox="0 0 540 130" preserveAspectRatio="none" aria-hidden="true">
      <path d="M0,12 Q270,62 540,86 V130 H0 Z" fill="var(--brand-blue)"/>
      <path d="M0,28 Q270,80 540,100 V130 H0 Z" fill="var(--brand-gray)"/>
    </svg>
    <div class="portrait" role="img" aria-label="Portrait photo of Tobias"></div>
    <div class="address-window"></div>
    <div class="contact">
      Mail: hello@brvsolutions.example | www.brvsolutions.example<br>
      24 Harbor Lane, Eastfield, 40210
    </div>
  </section>

  <section class="sheet envelope envelope--plain">
    <div class="company-name">BRV Solutions</div>
    <svg class="footer-band" viewBox="0 0 540 130" preserveAspectRatio="none" aria-hidden="true">
      <path d="M0,12 Q270,62 540,76 V130 H0 Z" fill="var(--brand-blue)"/>
      <path d="M0,28 Q270,80 540,90 V130 H0 Z" fill="var(--brand-gray)"/>
    </svg>
    <div class="portrait" role="img" aria-label="Portrait photo of Tobias"></div>
    <div class="contact">
      Call: xxxxxxxxx | Fax: xxxxxxx<br>
      Mail: hello@brvsolutions.example | www.brvsolutions.example<br>
      24 Harbor Lane, Eastfield, 40210
    </div>
  </section>

</body>
</html>
```